Simple and Approachable Cover for Pet Expo Company Page

Size: 2000 x 430; looking simply for words "Dunmore HR Consulting" and email address "DunmoreHRConsulting@brelvamail.com." This is for a cover photo for a company profile page for the Hollow Oak Expo, where I am a featured speaker on Employee Communications later this month. You can incorporate the attached photo to the left of the banner ad if you wish. The mood I wish to present is approachable, positive and simple.

Target Market(s)

small pet retail business owners

Industry/Entity Type

Pet Shop

Font styles to use
Serif
Sans Serif

Requirements
Must have
• Email address clearly defined/separated. Easy to read.
Nice to have
• I like the picture that I included; subtle pet paw background is also nice
Should not have
• No paid stock images

```html
<!DOCTYPE html>
<html lang="en">
<head>
<meta charset="utf-8">
<title>Dunmore HR Consulting — Cover Banner</title>
<link rel="stylesheet" href="https://fonts.googleapis.com/css2?family=League+Spartan:wght@600;700&display=swap">
<style>
  :root {
    --page-bg: #d3d2d2;
    --brand-blue: #1170bb;
    --brand-blue-deep: #0c5a9c;
    --accent-yellow: #f2cd35;
    --ink-dark: #1d1d1b;
    --white: #ffffff;
    --photo-green: #7f8f52;
    --photo-tree: #3f5a36;
    --photo-ground: #a08a5c;
  }
  html, body {
    margin: 0;
    padding: 0;
    width: 1200px;
    height: 798px;
    overflow: hidden;
    background: var(--page-bg);
  }
  .cover-banner {
    position: absolute;
    left: 40px;
    top: 278px;
    width: 1120px;
    height: 241px;
    box-shadow: 0 10px 24px rgba(0, 0, 0, 0.18);
  }
  .cover-banner svg {
    display: block;
    width: 100%;
    height: 100%;
  }
  .brand-name,
  .brand-tagline,
  .contact-email {
    font-family: "League Spartan", "Helvetica Neue", Arial, sans-serif;
  }
  .brand-name { font-weight: 700; font-size: 136px; fill: var(--white); }
  .brand-tagline { font-weight: 700; font-size: 70px; fill: var(--white); }
  .contact-email { font-weight: 600; font-size: 31px; fill: var(--ink-dark); }
</style>
</head>
<body>
  <div class="cover-banner">
    <svg viewBox="0 0 1510 325" xmlns="http://www.w3.org/2000/svg">
      <defs>
        <linearGradient id="blue-field" x1="0" y1="0" x2="1" y2="0">
          <stop offset="0.38" stop-color="var(--brand-blue-deep)"/>
          <stop offset="0.55" stop-color="var(--brand-blue)"/>
        </linearGradient>
        <linearGradient id="photo-tones" x1="0" y1="0" x2="0" y2="1">
          <stop offset="0" stop-color="var(--photo-tree)"/>
          <stop offset="0.45" stop-color="var(--photo-green)"/>
          <stop offset="1" stop-color="var(--photo-ground)"/>
        </linearGradient>
      </defs>

      <rect class="banner-field" width="1510" height="325" fill="url(#blue-field)"/>

      <path class="photo-frame"
            d="M135 0 L822 0 C722 60 632 180 607 325 L0 325 L0 108 C38 45 88 10 135 0 Z"
            fill="var(--white)"/>

      <path class="team-photo" role="img"
            aria-label="Photo of the two consultants sitting on grass in a park with their two hound dogs"
            d="M158 0 L802 0 C702 60 612 180 587 325 L0 325 L0 128 C40 60 95 18 158 0 Z"
            fill="url(#photo-tones)"/>

      <text class="brand-name" x="1100" y="148" text-anchor="middle">DUNMORE</text>
      <text class="brand-tagline" x="1100" y="213" text-anchor="middle">HR CONSULTING</text>

      <rect class="email-plate" x="780" y="235" width="642" height="62" rx="6" fill="var(--accent-yellow)"/>
      <text class="contact-email" x="1101" y="276" text-anchor="middle">DunmoreHRConsulting@brelvamail.com</text>
    </svg>
  </div>
</body>
</html>
```